Bespoke Branding Agency "Tidal Marks" seeks uplifting wordpress site

Looking for a SIMPLE, CLEAN, easy to manage wordpress site for our start-up Branding business. Our company is "Tidal Marks" and the site should reflect our vision.

We formed the company after making the decision never to work the average 9 to 5 work life again. We have vowed to never work in traditional corporate culture again. We are committed to a happier life with reduced stress and increased job satisfaction.

We want to build brands that make people happy.

We want to work with people who believe that you don’t have to be an asshole to be successful.

We believe that success should not be measured in monetary terms, but rather in happiness scores.

We believe in the Corwin Ashdale song lyric "Folks ought to grin often”.

We love sunflowers.

We prefer brevity over long wind.

We are motivated by creativity not money.

We love spending time with friends and family, and see this as our main priority in life.

We know life is short.

Industry/Entity Type

Business

```html
<!DOCTYPE html>
<html lang="en">
<head>
<meta charset="utf-8">
<title>Tidal Marks — Contact</title>
<link rel="stylesheet" href="https://fonts.googleapis.com/css2?family=Source+Sans+3:wght@400;600&family=Arimo:wght@400&display=swap">
<style>
  :root {
    --brand-pink: #ee1659;
    --field-white: #ffffff;
    --field-border: #2f2f2f;
    --placeholder-grey: #a9a9a9;
    --button-ink: #262626;
    --footer-dark: #232323;
    --footer-darker: #161616;
    --footer-text: #ffffff;
    --mark-fill: #ee1659;
  }
  * { box-sizing: border-box; margin: 0; padding: 0; }
  html, body {
    width: 1200px;
    height: 900px;
    overflow: hidden;
    background: var(--footer-darker);
  }
  .page {
    position: relative;
    width: 1200px;
    height: 900px;
    overflow: hidden;
    font-family: "Source Sans 3", sans-serif;
  }

  /* Contact section */
  .contact {
    position: absolute;
    left: 0; top: 0;
    width: 1200px;
    height: 572px;
    background: var(--brand-pink);
  }
  .contact__notch {
    position: absolute;
    left: 532px; top: 0;
  }
  .contact__title {
    position: absolute;
    left: 0; top: 86px;
    width: 1200px;
    text-align: center;
    color: var(--field-white);
    font-weight: 400;
    font-size: 92px;
    line-height: 110px;
    letter-spacing: 1px;
  }
  .field {
    position: absolute;
    background: var(--field-white);
    border: 2px solid var(--field-border);
    color: var(--placeholder-grey);
    font-size: 22px;
    padding-left: 22px;
  }
  .field--message { left: 44px; top: 256px; width: 524px; height: 224px; padding-top: 24px; }
  .field--name    { left: 628px; top: 256px; width: 524px; height: 63px; line-height: 59px; }
  .field--email   { left: 628px; top: 331px; width: 524px; height: 63px; line-height: 59px; }
  .send-button {
    position: absolute;
    left: 628px; top: 411px;
    width: 240px; height: 69px;
    background: var(--field-white);
    border: 2px solid var(--field-border);
    color: var(--button-ink);
    font-family: "Source Sans 3", sans-serif;
    font-weight: 600;
    font-size: 18px;
    text-align: center;
    line-height: 65px;
  }

  /* Footer */
  .footer {
    position: absolute;
    left: 0; top: 572px;
    width: 1200px;
    height: 328px;
  }
  .footer__texture {
    position: absolute;
    inset: 0;
    background: linear-gradient(180deg, var(--footer-dark), var(--footer-darker));
  }
  .footer__mark {
    position: absolute;
    left: 533px; top: 81px;
    width: 130px; height: 130px;
    border-radius: 50%;
    background: var(--mark-fill);
  }
  .footer__name {
    position: absolute;
    left: 0; top: 244px;
    width: 1200px;
    text-align: center;
    color: var(--footer-text);
    font-family: "Arimo", sans-serif;
    font-size: 46px;
    line-height: 56px;
  }
  .footer__address {
    position: absolute;
    left: 0; top: 306px;
    width: 1200px;
    text-align: center;
    color: var(--footer-text);
    font-family: "Arimo", sans-serif;
    font-size: 32px;
    line-height: 40px;
  }
</style>
</head>
<body>
<div class="page">
  <section class="contact">
    <svg class="contact__notch" width="132" height="57" viewBox="0 0 132 57" aria-hidden="true">
      <polygon points="0,0 132,0 66,56" fill="#ffffff"/>
    </svg>
    <h1 class="contact__title">CONTACT</h1>
    <div class="field field--message">Message</div>
    <div class="field field--name">Name</div>
    <div class="field field--email">Email</div>
    <div class="send-button">SEND MESSAGE</div>
  </section>

  <footer class="footer">
    <div class="footer__texture" role="img" aria-label="Dark woven carbon-fibre texture background"></div>
    <div class="footer__mark" aria-hidden="true"></div>
    <p class="footer__name">TIDAL MARKS</p>
    <p class="footer__address">2140 Harbor Lane |Suite 318</p>
  </footer>
</div>
</body>
</html>
```